Brand-new Pediatric Dental Practice needs a website

We are a brand-new dental practice that will specialize in treating children. We want a gorgeous and easily navigable dental practice website that would make a good first impression to potential patients and their parents. It should be modern, SEO-friendly, mobile responsive, and optimized to win new patients.

Target Market(s)

Parents

Industry/Entity Type

Healthcare/Dentistry

Coding

Coded - Design and coding required

Number of Pages Required

4 page

Requirements
Must have
• Use the Wix website building platform. 4 pages: home, meet our dentists, services, contact us
Nice to have
• has a link to our facebook, instagram

```html
<!DOCTYPE html>
<html lang="en">
<head>
<meta charset="utf-8">
<title>Maple Grove Pediatric Dentistry</title>
<link href="https://fonts.googleapis.com/css2?family=Lexend:wght@400;500&family=Quicksand:wght@400;500;600;700&display=swap" rel="stylesheet">
<style>
:root{
  --navy:#1b4680;
  --band:#234f8e;
  --blue:#2b87e3;
  --ink:#1b1f2a;
  --muted:#6b7280;
  --soft:#f2f4f9;
  --white:#ffffff;
  --line:#d8dde6;
}
*{box-sizing:border-box;margin:0;padding:0}
html,body{width:1200px;height:3655px;overflow:hidden}
body{position:relative;background:var(--white);font-family:"Quicksand",sans-serif;color:var(--ink)}
.abs{position:absolute}
h1,h2,h3,h4{font-family:"Lexend",sans-serif;font-weight:500}
a{color:inherit;text-decoration:none}

/* top bar */
.topbar{left:0;top:0;width:1200px;height:48px;background:var(--navy);color:var(--white);font-size:14px;font-weight:600}
.topbar .contact{position:absolute;left:86px;top:15px;display:flex;gap:24px;align-items:center}
.topbar .contact span{display:flex;gap:8px;align-items:center}
.dot{display:inline-block;border-radius:50%}
.topbar .social{position:absolute;right:86px;top:13px;display:flex;gap:8px}
.topbar .social .dot{width:22px;height:22px;background:var(--white)}

/* header */
.header{left:0;top:48px;width:1200px;height:109px;background:var(--white);border-bottom:1px solid #eef0f4}
.brand{position:absolute;display:flex;align-items:center;gap:10px;font-family:"Quicksand",sans-serif;font-weight:600;color:#3d4652}
.header .brand{left:86px;top:38px;font-size:22px}
.brand .mark{width:28px;height:28px;border-radius:50%;background:#7cc49a}
.nav{position:absolute;right:138px;top:44px;display:flex;gap:38px;font-size:16px;font-weight:600}
.search{position:absolute;right:86px;top:45px}

/* hero */
.hero{left:0;top:157px;width:1200px;height:636px;background:linear-gradient(100deg,#cfd6de 0%,#9eb3c9 35%,#e8e2da 60%,#c8bcae 100%)}
.hero-card{left:86px;top:316px;width:630px;height:384px;background:rgba(27,82,150,.88);border-radius:8px;color:var(--white);padding:44px 46px}
.eyebrow{display:flex;align-items:center;gap:10px;font-size:13px;font-weight:700;letter-spacing:.2px;text-transform:uppercase}
.eyebrow::before{content:"";width:30px;height:1px;background:currentColor}
.hero-card h1{font-size:46px;line-height:55px;margin-top:18px}
.hero-card p{font-size:14px;line-height:21px;margin-top:22px;width:450px}
.btn{display:inline-block;background:var(--blue);color:var(--white);font-size:13px;font-weight:600;text-transform:uppercase;border-radius:4px;text-align:center}
.hero-card .btn{margin-top:26px;width:137px;height:46px;line-height:46px}

/* section headings */
.label{font-size:13px;font-weight:700;text-transform:uppercase;display:flex;align-items:center;gap:10px}
.label.after::after{content:"";width:30px;height:1px;background:currentColor}
.label.before::before{content:"";width:30px;height:1px;background:currentColor}
.title{font-size:42px;line-height:51px;color:var(--ink)}
.view-all{width:137px;height:46px;line-height:46px}

/* services */
.service{width:237px;height:305px;background:var(--white);border-radius:6px;box-shadow:0 2px 12px rgba(20,40,80,.09);border-bottom:3px solid var(--navy);text-align:center;padding:14px 13px}
.service .photo{height:156px;border-radius:2px}
.service h3{font-size:20px;margin-top:24px}
.service p{font-size:13.5px;line-height:17px;color:var(--muted);margin:10px 14px 0}

/* about */
.about{left:0;top:1428px;width:1200px;height:711px;background:var(--soft)}
.about .lead{font-size:13.5px;font-weight:700;line-height:21px}
.about .body{font-size:13.5px;line-height:21px;color:var(--muted)}
.feature h4{font-size:20px;margin-top:14px}
.feature p{font-size:14px;line-height:21px;color:var(--muted);margin-top:10px}
.frame{left:740px;top:1568px;width:396px;height:461px;border:6px solid var(--blue);border-radius:12px}
.about-photo{left:713px;top:1541px;width:379px;height:444px;border-radius:6px;background:linear-gradient(135deg,#d9dde2 0%,#e8b838 45%,#2d3a52 80%,#cfd4da 100%)}

/* dentists */
.dentist{width:325px;height:452px;background:var(--white);border-radius:6px;box-shadow:0 2px 12px rgba(20,40,80,.09);border-bottom:3px solid var(--navy);text-align:center;overflow:hidden}
.dentist .photo{height:293px}
.dentist h3{font-size:21px;margin-top:30px}
.dentist .role{font-size:14px;color:var(--muted);margin-top:8px}
.dentist .social{display:flex;gap:11px;justify-content:center;margin-top:18px}
.dentist .social .dot{width:43px;height:43px;background:var(--blue)}

/* cta */
.cta{left:0;top:2965px;width:1200px;height:234px;background:var(--band)}
.cta h2{position:absolute;left:86px;top:57px;color:var(--white);font-size:42px;line-height:51px}
.cta .btn{position:absolute;left:977px;top:93px;width:137px;height:46px;line-height:46px;background:var(--white);color:var(--navy)}

/* footer */
.footer .brand{left:86px;top:3330px;font-size:22px}
.footer .about-text{left:86px;top:3412px;width:260px;font-size:13px;line-height:21px;font-weight:600}
.fcol h4{font-size:21px;font-weight:400}
.fcol ul{list-style:none;margin-top:32px;font-size:13.5px;font-weight:600}
.fcol li{margin-bottom:16px}
.fcol.contact li{margin-bottom:12px;line-height:19px}
.rule{left:86px;top:3575px;width:1027px;height:1px;background:var(--line)}
.copy{left:86px;top:3595px;font-size:13px;font-weight:600}
.footer-social{left:1054px;top:3592px;display:flex;gap:12px}
.footer-social .dot{width:22px;height:22px;background:var(--navy)}
</style>
</head>
<body>

<div class="abs topbar">
  <div class="contact">
    <span>
      <svg width="12" height="12" viewBox="0 0 24 24" fill="#fff"><path d="M6.6 10.8a15.2 15.2 0 0 0 6.6 6.6l2.2-2.2c.3-.3.7-.4 1-.2 1.1.4 2.3.6 3.6.6.6 0 1 .4 1 1V20c0 .6-.4 1-1 1A17 17 0 0 1 3 4c0-.6.4-1 1-1h3.5c.6 0 1 .4 1 1 0 1.3.2 2.5.6 3.6.1.3 0 .7-.2 1z"/></svg>
      +1800-555-0147
    </span>
    <span>
      <svg width="14" height="11" viewBox="0 0 24 18" fill="#fff"><path d="M1 1h22v16H1z"/><path d="M1 1l11 8 11-8" stroke="#1b4680" stroke-width="2" fill="none"/></svg>
      hello@maplegrove-kids.com
    </span>
  </div>
  <div class="social"><span class="dot" aria-label="Social profile link"></span><span class="dot" aria-label="Social profile link"></span></div>
</div>

<header class="abs header">
  <div class="brand"><span class="mark"></span>maple grove</div>
  <nav class="nav"><a>Home</a><a>Meet Our Dentists</a><a>Services</a><a>Contact Us</a></nav>
  <svg class="search" width="20" height="20" viewBox="0 0 24 24" fill="none" stroke="#1b1f2a" stroke-width="2"><circle cx="10" cy="10" r="7"/><path d="M15 15l6 6"/></svg>
</header>

<section class="abs hero" role="img" aria-label="Young girl smiling in a dentist chair while a dentist holds a dental model"></section>
<div class="abs hero-card">
  <div class="eyebrow">Partnership for health</div>
  <h1>Modern Dentistry with Unique Technologies</h1>
  <p>Lorem Ipsum is simply dummy text of the printing and typesetting industry. Lorem Ipsum has been the industry's standard dummy text ever since Athe 1500s</p>
  <a class="btn">Read more</a>
</div>

<!-- services -->
<div class="abs label after" style="left:86px;top:902px">Our services</div>
<h2 class="abs title" style="left:84px;top:932px">Explore Our Main Service</h2>
<a class="abs btn view-all" style="left:977px;top:936px">View all</a>

<article class="abs service" style="left:86px;top:1011px">
  <div class="photo" role="img" aria-label="Dentist examining a child in an orange chair" style="background:linear-gradient(135deg,#b9cfe0,#f08a1e 55%,#6b8fb3)"></div>
  <h3>Dental Filling</h3>
  <p>There are many variations of pas of Lorem Ipsum available.</p>
</article>
<article class="abs service" style="left:349px;top:1011px">
  <div class="photo" role="img" aria-label="Hands holding a tooth model showing the root" style="background:linear-gradient(135deg,#eef2f6,#e7b7a0 50%,#d9e3ee)"></div>
  <h3 style="margin-top:27px">Root Canal</h3>
  <p>There are many variations of pas of Lorem Ipsum available.</p>
</article>
<article class="abs service" style="left:612px;top:1011px">
  <div class="photo" role="img" aria-label="Girl sitting in a dental chair in a bright clinic" style="background:linear-gradient(135deg,#e6eaee,#8ea7bd 50%,#eef0f2)"></div>
  <h3>Dental Implant</h3>
  <p>There are many variations of pas of Lorem Ipsum available.</p>
</article>
<article class="abs service" style="left:877px;top:1011px">
  <div class="photo" role="img" aria-label="Hands holding a jaw model fitted with braces" style="background:linear-gradient(135deg,#d5e4f1,#e58a8f 50%,#eef3f8)"></div>
  <h3>Braces &amp; Aligners</h3>
  <p>There are many variations of pas of Lorem Ipsum available.</p>
</article>

<!-- about -->
<section class="abs about"></section>
<div class="abs label before" style="left:86px;top:1578px">What about us</div>
<h2 class="abs title" style="left:84px;top:1600px">We Provide the Best<br>Dental Service</h2>
<p class="abs lead" style="left:86px;top:1718px;width:548px">Lorem Ipsum is simply dummy text of the printing and typesetting industry. Lorem Ipsum has been the industry's standard dummy text ever since the 1500s, when an unknown printer</p>
<p class="abs body" style="left:86px;top:1800px;width:515px">Lorem Ipsum is simply dummy text of the printing and typesetting industry. Lorem Ipsum has been the industry's standard dummy text</p>
<div class="abs feature" style="left:86px;top:1866px;width:260px">
  <svg width="40" height="34" viewBox="0 0 40 34" fill="none" stroke="#2b87e3" stroke-width="1.6"><path d="M4 8c0-5 6-6 9-3 3-3 9-2 9 3 0 6-2 8-3 14-1 4-3 4-4 0l-2-6-2 6c-1 4-3 4-4 0C5 16 4 14 4 8z"/><circle cx="28" cy="22" r="8"/><path d="M28 18v8M24 22h8"/></svg>
  <h4>Dental Prevention</h4>
  <p>Lorem Ipsum is simply dummy text of the printing</p>
</div>
<div class="abs feature" style="left:389px;top:1866px;width:260px">
  <svg width="40" height="34" viewBox="0 0 40 34" fill="none" stroke="#2b87e3" stroke-width="1.6"><path d="M8 8c0-6 8-7 12-3 4-4 12-3 12 3 0 7-3 10-4 18-1 5-4 5-5 0l-3-7-3 7c-1 5-4 5-5 0C11 18 8 15 8 8z"/><path d="M3 30l8-8M6 4l3 3"/></svg>
  <h4>Dental Services</h4>
  <p>Lorem Ipsum is simply dummy text of the printing</p>
</div>
<div class="abs frame"></div>
<div class="abs about-photo" role="img" aria-label="Young boy sitting in a yellow dental chair"></div>

<!-- dentists -->
<div class="abs label before" style="left:86px;top:2248px">Our dentist</div>
<h2 class="abs title" style="left:84px;top:2270px">Meet Our Specialized and<br>Experienced Dentist</h2>
<a class="abs btn view-all" style="left:977px;top:2323px">View all</a>

<article class="abs dentist" style="left:86px;top:2398px">
  <div class="photo" role="img" aria-label="Portrait of a male dentist in a white coat holding dental tools" style="background:linear-gradient(180deg,#f2f3f5,#dfe5ec)"></div>
  <h3>Dr. Elena Marsh</h3>
  <div class="role">Prosthodontics Dentist</div>
  <div class="social"><span class="dot" aria-label="Social profile link"></span><span class="dot" aria-label="Social profile link"></span></div>
</article>
<article class="abs dentist" style="left:437px;top:2398px">
  <div class="photo" role="img" aria-label="Portrait of a female dentist in blue scrubs" style="background:linear-gradient(135deg,#5fc9dc,#2aa7c4 60%,#4a86c9)"></div>
  <h3>Dr. Priya Holloway</h3>
  <div class="role">Prosthodontics Dentist</div>
  <div class="social"><span class="dot" aria-label="Social profile link"></span><span class="dot" aria-label="Social profile link"></span></div>
</article>
<article class="abs dentist" style="left:788px;top:2398px">
  <div class="photo" role="img" aria-label="Portrait of a male dentist holding a jaw model" style="background:linear-gradient(180deg,#e9ebee,#d6dade)"></div>
  <h3>Dr. Tomas Reyes</h3>
  <div class="role">Prosthodontics Dentist</div>
  <div class="social"><span class="dot" aria-label="Social profile link"></span><span class="dot" aria-label="Social profile link"></span></div>
</article>

<!-- cta -->
<section class="abs cta">
  <h2>A great place of medical<br>hospital center &amp; dental care</h2>
  <a class="btn">Contact us</a>
</section>

<!-- footer -->
<footer class="footer">
  <div class="abs brand"><span class="mark"></span>maple grove</div>
  <p class="abs about-text">It helps designers plan out where the content will sit, the content to be written and approved.</p>
  <div class="abs fcol" style="left:436px;top:3322px">
    <h4>Main Menu</h4>
    <ul><li>Home</li><li>About Us</li><li>Meet Our Dentists</li><li>Services</li><li>Contact</li></ul>
  </div>
  <div class="abs fcol" style="left:645px;top:3322px">
    <h4>Quick Links</h4>
    <ul><li>FAQ</li><li>Doctors</li><li>Departments</li><li>Events</li><li>Member</li></ul>
  </div>
  <div class="abs fcol contact" style="left:855px;top:3322px;width:265px">
    <h4>Contact</h4>
    <ul><li>Call : +1800-555-0147</li><li>Email : hello@maplegrove-kids.com</li><li>Location : Lorem ipsum dolor sit amet, consectetur adipiscing elit.</li></ul>
  </div>
  <div class="abs rule"></div>
  <p class="abs copy">Copyright 2022 Maple Grove. All Rights Reserved</p>
  <div class="abs footer-social"><span class="dot" aria-label="Social profile link"></span><span class="dot" aria-label="Social profile link"></span></div>
</footer>

</body>
</html>
```